Foot doctor needs feet friendly business cards.

Business cards for Podiatrist. Needs to look professional and modern. Back side put an appointment card, and try to put a little basic street map somewhere on card along with all of our contact info below:

Marcus Hollend, DPM, Inc.
Diplomate, National Council of Lower Limb Practice
Call: 1.877.Walk.482
1.555.238.6149
Fax: 1.555.871.3902
Email: info@DrHollend.example
Web: www.DrHollend.example
2741 N. Harbor Ln. Suite 208
Linden Cove, WA 90413

```html
<!DOCTYPE html>
<html lang="en">
<head>
<meta charset="utf-8">
<title>Marcus Hollend, DPM – Business &amp; Appointment Card</title>
<link href="https://fonts.googleapis.com/css2?family=Lato:wght@400;700;900&display=swap" rel="stylesheet">
<style>
  :root {
    --bg: #2b2b2d;
    --card: #f7f8f8;
    --band: #c8e2ed;
    --accent: #3b8fc3;
    --ink: #1f2326;
    --ink-soft: #3a3f44;
    --placeholder: #c9ced2;
    --map-a: #e7e3da;
    --map-b: #d9dccf;
  }
  * { box-sizing: border-box; margin: 0; padding: 0; }
  html, body { width: 1200px; height: 997px; overflow: hidden; }
  body {
    background: var(--bg);
    font-family: "Lato", sans-serif;
    color: var(--ink);
    position: relative;
  }
  .card {
    position: absolute;
    left: 220px;
    width: 760px;
    height: 434px;
    background: var(--card);
    overflow: hidden;
    box-shadow: 0 14px 30px rgba(0,0,0,.45);
  }
  .card--front { top: 44px; }
  .card--back { top: 518px; }

  /* front */
  .front__top-band { position: absolute; left: 0; top: 0; width: 100%; height: 66px; background: var(--band); }
  .front__bottom-band { position: absolute; left: 0; bottom: 0; width: 100%; height: 56px; background: var(--band); }
  .front__name {
    position: absolute; left: 100px; top: 20px; width: 330px;
    font-weight: 900; font-size: 26px; letter-spacing: .3px; text-transform: uppercase;
    white-space: nowrap; line-height: 30px;
  }
  .front__name-suffix { font-weight: 400; font-size: 17px; color: var(--accent); text-transform: none; margin-left: 6px; letter-spacing: 0; }
  .front__map {
    position: absolute; left: 440px; top: 22px; width: 304px; height: 356px;
    background: linear-gradient(160deg, var(--map-a), var(--map-b));
  }
  .front__body { position: absolute; left: 34px; top: 88px; width: 396px; }
  .front__credential { font-size: 18px; line-height: 1.3; text-align: center; width: 300px; }
  .front__services { list-style: none; margin-top: 24px; }
  .front__services li { display: flex; align-items: center; gap: 10px; font-size: 18px; margin-bottom: 6px; }
  .front__contacts { list-style: none; margin-top: 20px; }
  .front__contacts li { display: flex; align-items: center; gap: 14px; font-size: 18px; margin-bottom: 10px; white-space: nowrap; }
  .front__contacts svg { flex: none; width: 22px; }
  .front__web { position: absolute; left: 34px; bottom: 16px; font-weight: 700; font-size: 18px; }
  .front__address { position: absolute; right: 20px; bottom: 16px; font-weight: 700; font-size: 18px; }

  /* back */
  .back__top-band { position: absolute; left: 0; top: 0; width: 100%; height: 26px; background: var(--band); }
  .back__bottom-band {
    position: absolute; left: 0; bottom: 0; width: 100%; height: 78px; background: var(--band);
    display: flex; align-items: center; justify-content: center; text-align: center;
    font-size: 16px; line-height: 1.35; color: var(--ink-soft); padding: 0 60px;
  }
  .back__title {
    position: absolute; left: 0; width: 100%; top: 44px; text-align: center;
    font-weight: 900; font-size: 20px; text-transform: uppercase; letter-spacing: .5px;
  }
  .back__title span { border-bottom: 2px solid var(--ink); padding-bottom: 1px; }
  .field { position: absolute; border-bottom: 2px solid var(--ink-soft); font-size: 19px; color: var(--placeholder); height: 40px; display: flex; align-items: flex-end; padding-bottom: 4px; }
  .field--name { left: 60px; right: 60px; top: 82px; padding-left: 200px; }
  .field--date { left: 60px; width: 300px; top: 232px; padding-left: 10px; }
  .field--time { left: 390px; right: 60px; top: 232px; padding-left: 10px; }
  .field--location { left: 60px; right: 60px; top: 296px; padding-left: 210px; }
  .days { position: absolute; left: 60px; right: 60px; top: 160px; display: flex; justify-content: space-between; }
  .check { display: flex; align-items: center; gap: 6px; font-weight: 700; font-size: 18px; color: var(--ink-soft); }
  .check__box { width: 26px; height: 26px; border: 3px solid var(--ink); border-radius: 5px; background: #fff; }
  .meridiem { position: absolute; right: 60px; top: 210px; display: flex; gap: 18px; }
</style>
</head>
<body>

<section class="card card--front" aria-label="Business card front">
  <div class="front__top-band"></div>
  <div class="front__bottom-band"></div>
  <div class="front__map" role="img" aria-label="Basic street map showing the office location near the freeway"></div>
  <h1 class="front__name">Marcus Hollend<span class="front__name-suffix">DPM, Inc.</span></h1>

  <div class="front__body">
    <p class="front__credential">Diplomate, National Council of Lower Limb Practice</p>
    <ul class="front__services">
      <li><svg width="16" height="14" viewBox="0 0 16 14"><path d="M1 7 L6 12 L15 1" fill="none" stroke="var(--accent)" stroke-width="3"/></svg>Heel Pain Relief Specialist</li>
      <li><svg width="16" height="14" viewBox="0 0 16 14"><path d="M1 7 L6 12 L15 1" fill="none" stroke="var(--accent)" stroke-width="3"/></svg>Nail Fungus Laser Treatments</li>
    </ul>
    <ul class="front__contacts">
      <li><svg height="18" viewBox="0 0 22 18" aria-label="Phone"><path d="M2 8 C2 2 20 2 20 8 L16 8 L15 5 L7 5 L6 8 Z M5 10 H17 L19 17 H3 Z" fill="var(--accent)"/></svg>1.877.Walk.482 / 1.555.238.6149</li>
      <li><svg height="18" viewBox="0 0 22 18" aria-label="Fax"><rect x="6" y="1" width="10" height="5" fill="var(--accent)"/><rect x="1" y="6" width="20" height="8" rx="2" fill="var(--accent)"/><rect x="6" y="11" width="10" height="6" fill="var(--accent)"/></svg>1.555.871.3902</li>
      <li><svg height="16" viewBox="0 0 22 16" aria-label="Email"><rect x="1" y="1" width="20" height="14" fill="var(--accent)"/><path d="M1 1 L11 9 L21 1" fill="none" stroke="#fff" stroke-width="1.5"/></svg>info@DrHollend.example</li>
    </ul>
  </div>

  <p class="front__web">www.DrHollend.example</p>
  <p class="front__address">2741 N. Harbor Ln. Suite 208, Linden Cove, WA 90413</p>
</section>

<section class="card card--back" aria-label="Appointment card">
  <div class="back__top-band"></div>
  <h2 class="back__title"><span>Appointment Card</span></h2>
  <div class="field field--name">Patient Name</div>
  <div class="days">
    <span class="check">Mon<i class="check__box"></i></span>
    <span class="check">Tue<i class="check__box"></i></span>
    <span class="check">Wed<i class="check__box"></i></span>
    <span class="check">Thu<i class="check__box"></i></span>
    <span class="check">Fri<i class="check__box"></i></span>
    <span class="check">Sat<i class="check__box"></i></span>
  </div>
  <div class="field field--date">Date:</div>
  <div class="field field--time">Time:</div>
  <div class="meridiem">
    <span class="check">AM<i class="check__box"></i></span>
    <span class="check">PM<i class="check__box"></i></span>
  </div>
  <div class="field field--location">Location</div>
  <p class="back__bottom-band">If you are unable to keep your appointment, pl contact us as soon as possible call: 1.555.240.7731</p>
</section>

</body>
</html>
```